Business Card Design Project - veltramo

We are building an agency for innovative solutions in marketing, education and events to pharmaceutical companies, physicians, medical societies, patient advocacy groups. We want to become a reference in this market in Brazil as the most boutique agency here. We deal with every detail with a lot of love and caring for what we do like craftsmen.
Our card must show innovation and inspiration. Yet should be clean. Something like Swiss design, quince design, etc.
Updates
Reason: I think the initial time was too short. I believe with more time you can exceed expectations. I'm liking a lot this experience
Target Market(s)
Pharmaceutical companies, doctors and patients
Industry/Entity Type
Pharmaceutical
Font styles to use
Other font styles liked:
- Helvetia family
Colors
Designer to choose colors to be used in the design.
Requirements
Must have
- Modern, clean,
Nice to have
- Innovative idea to show
Should not have
- Not too appear too much Comercial. Must be modern but sober.

```html
<!DOCTYPE html>
<html lang="en">
<head>
<meta charset="utf-8">
<title>veltramo – business card</title>
<link rel="stylesheet" href="https://fonts.googleapis.com/css2?family=Roboto:wght@300;400&display=swap">
<style>
  :root {
    --page: #ffffff;
    --frame: #1a1a1a;
    --card: #000000;
    --accent: #cc2a00;
    --logo-red: #d0241a;
    --text-light: #ffffff;
    --text-muted: #a8a8a8;
    --band-dark: #6e6e6e;
    --band-light: #b4b4b4;
  }
  * { margin: 0; padding: 0; box-sizing: border-box; }
  html, body { width: 1200px; height: 900px; overflow: hidden; background: var(--page); }
  body { font-family: "Roboto", "Helvetica Neue", Arial, sans-serif; font-weight: 300; }

  .sheet {
    position: relative;
    width: 1200px; height: 900px;
    border: 1px solid var(--frame);
    background: var(--page);
  }

  .card {
    position: absolute;
    left: 360px;
    width: 464px; height: 273px;
    background: var(--card);
  }
  .card--front { top: 94px; }
  .card--back { top: 457px; }

  .wordmark {
    position: absolute;
    transform: translate(-50%, -50%);
    color: var(--logo-red);
    font-weight: 300;
    font-size: 24px;
    letter-spacing: 0.5px;
    white-space: nowrap;
  }
  .card--front .wordmark { left: 232px; top: 121px; }
  .card--back .wordmark { left: 369px; top: 93px; }

  .card__url {
    position: absolute;
    left: 0; right: 0; top: 171px;
    text-align: center;
    padding-right: 10px;
    color: var(--text-light);
    font-size: 11.5px;
    font-weight: 300;
  }

  .accent-block {
    position: absolute;
    left: 0; top: 0;
    width: 290px; height: 127px;
    background: var(--accent);
  }
  .holder {
    position: absolute;
    right: 32px; bottom: 12px;
    text-align: right;
    color: var(--text-light);
    font-size: 14.5px;
    font-weight: 300;
    line-height: 16px;
  }

  .contact {
    position: absolute;
    right: 206px; top: 137px;
    list-style: none;
    text-align: right;
    color: var(--text-muted);
    font-size: 12.5px;
    line-height: 18.5px;
    white-space: nowrap;
  }
  .contact__item { display: flex; justify-content: flex-end; align-items: center; gap: 6px; }
  .contact__icon { width: 9px; height: 9px; fill: var(--text-muted); }

  .presentation-band {
    position: absolute;
    left: 0; bottom: 0;
    width: 1198px; height: 111px;
    background: linear-gradient(180deg, var(--band-dark) 0%, var(--band-light) 55%, #9c9c9c 100%);
  }
</style>
</head>
<body>
<main class="sheet">

  <section class="card card--front" aria-label="Card front">
    <div class="wordmark">veltramo</div>
    <p class="card__url">www.veltramo.com</p>
  </section>

  <section class="card card--back" aria-label="Card back">
    <div class="accent-block">
      <p class="holder">Lena Marsh<br>CEO</p>
    </div>
    <div class="wordmark">veltramo</div>
    <ul class="contact">
      <li class="contact__item">27 Harbor ave. 10931 - Fla</li>
      <li class="contact__item">
        <svg class="contact__icon" viewBox="0 0 10 10" aria-hidden="true"><rect x="2" y="0" width="6" height="10" rx="1"/><rect x="3" y="1.2" width="4" height="3" fill="#000"/></svg>
        1-40258316
      </li>
      <li class="contact__item">
        <svg class="contact__icon" viewBox="0 0 10 8" aria-hidden="true"><rect x="0" y="1" width="10" height="6"/><path d="M0 1 L5 4.5 L10 1" stroke="#000" stroke-width="0.8" fill="none"/></svg>
        lena@veltramo.com
      </li>
    </ul>
  </section>

  <div class="presentation-band" role="img" aria-label="Grey scratched concrete texture band"></div>

</main>
</body>
</html>
```